Ice Cream Product Packaging - Bucket and Lid

We need some high quality packaging designed for a client who manufactures and sells 'healthy' Ice Cream (low calories, high protein etc).
The logo needs to be designed also which is the main image of the packaging.
Prefer lower case for main fonts. needs to look elegant, naughty and high end.
There are 2 flavours at this stage - chocolate and vanilla.
Target market is for adults - 18-40, fitness, gym etc.

There are 2 sizes but let's just get the largest one sorted first?

Title: "lumé" (means 'kiss' in French) - they want an image of some pronounced red lips behind the name. The red lips will be their main brand identity/logo.. With some chocolate dripping out of the side. (brown for the chocolate flavour and a cream colour for the vanilla flavour). Maybe a faded image of an attactive womans face - mainly the lips and chin (if chin is necessary?!) - the text "Ice Creamery" can be in a small font underneath

Subtitle: Can go above (or below) main title: "naughty & healthy" followed on the next line by: "Low Calories + High Protein" (they are thinking about spelling 'naughty' incorrectly - like "nauty".. I'm not sure about this though..what do you think?!) This text can be in gold or silver perhaps and a handwriting font to give it that high end look? Up to you.

Background - whatever you think.. some sort of nice textured background perhaps? brown shades for the chocolate flavour, creamy/yellowy shades for the vanilla flavour. Can we also have some ice cream 'dripping' from the top.

There will be a section of 6 lips icons that will say: Gluten Free, High Protein, Low Calories, Lactose Free, No Added Sugar, Digestive Enzyme. These icons can go down the side of the bucket.

Colours: Red, black, brown (for choc), cream (for vanilla), gold and/or silver, white or cream etc etc.
Bucket for chocolate will be black so there is a black lip at the top (tamper proof seal). Bucket for Vanilla is white so will be white at the top - tamper proof seal. incorporate those colurs.

We also need some room for ingredients text, barcode and some company info.

Please see the files attachedfor a rough version. Doesn't need to be exactly the same but something similar would be fantastic.

Also attached are the 2 ice cream bucket sizes, their dimensions and the Lid size.
Lid will just be a copy of the main image on the bucket.

Target Market(s)

adults, 18-40, fitness, healthy, gym, foodies

Font styles to use
Sans Serif
Script

Colors
ec1f27
f04a50
fff3d1
ffffff
1b1b1b

Requirements
Must have
• Elegant look, high end, healthy ice cream, red lips... see description for more detailed info
Nice to have
• see description for more detailed info
Should not have

```html
<!DOCTYPE html>
<html lang="en">
<head>
<meta charset="utf-8">
<title>lumé ice creamery – packaging set</title>
<link rel="stylesheet" href="https://fonts.googleapis.com/css2?family=Questrial&family=Cookie&display=swap">
<style>
  :root {
    --page: #fcc3b4;
    --ink-brown: #3b1f1a;
    --lip-red: #c62a2f;
    --lip-deep: #8e1a20;
    --choc-1: #a08474;
    --choc-2: #b5927c;
    --choc-3: #8c7468;
    --van-1: #fff6c4;
    --van-2: #fdeea0;
    --van-3: #fbf3d0;
    --band-1: #5e4741;
    --band-2: #8a726a;
    --panel: rgba(255, 255, 255, 0.72);
    --choc-copy: #d9a066;
    --van-copy: #6b3a2c;
  }
  * { box-sizing: border-box; margin: 0; padding: 0; }
  html, body { width: 1200px; height: 1200px; overflow: hidden; }
  body { background: var(--page); }
  .canvas { position: relative; width: 1200px; height: 1200px; background: var(--page); overflow: hidden; }

  /* surfaces */
  .surface { position: absolute; overflow: hidden; }
  .surface--choc { background: radial-gradient(ellipse at 30% 30%, var(--choc-2), var(--choc-1) 60%, var(--choc-3)); }
  .surface--vanilla { background: radial-gradient(ellipse at 35% 35%, var(--van-3), var(--van-1) 55%, var(--van-2)); }
  .bucket-label { width: 708px; height: 275px; }
  .lid { width: 292px; height: 292px; }

  .bucket-label--choc { left: 39px; top: 100px; }
  .lid--choc { left: 792px; top: 100px; }
  .lid--vanilla { left: 102px; top: 853px; }
  .bucket-label--vanilla { left: 450px; top: 868px; }

  /* brand lockup: plain circle + name, one font, one colour, one weight */
  .logo {
    position: absolute; display: flex; align-items: center; justify-content: center;
    gap: 0.22em; transform: translate(-50%, -50%);
    font-family: "Questrial", sans-serif; font-weight: 400; color: var(--ink-brown);
    line-height: 1; white-space: nowrap;
  }
  .logo__dot {
    width: 1.15em; height: 1.15em; border-radius: 50%; flex: none;
    background: radial-gradient(circle at 40% 35%, var(--lip-red), var(--lip-deep));
  }
  .logo__name { font-size: 1em; }

  .logo--hero-choc { font-size: 140px; left: 300px; top: 660px; }
  .logo--hero-vanilla { font-size: 148px; left: 900px; top: 680px; }
  .bucket-label .logo { font-size: 52px; left: 150px; top: 128px; }
  .lid .logo { font-size: 56px; left: 146px; top: 146px; }

  /* claims list */
  .claims { position: absolute; left: 300px; top: 32px; list-style: none; }
  .claims li {
    display: flex; align-items: center; gap: 10px; height: 30px;
    font-family: "Cookie", cursive; font-size: 27px;
  }
  .bucket-label--choc .claims li { color: var(--choc-copy); }
  .bucket-label--vanilla .claims li { color: var(--van-copy); }
  .claims i { width: 26px; height: 17px; border-radius: 50%; flex: none; }
  .claims li:nth-child(1) i { background: #d9383c; }
  .claims li:nth-child(2) i { background: #b83d40; }
  .claims li:nth-child(3) i { background: #9c3636; }
  .claims li:nth-child(4) i { background: #7e3230; }
  .claims li:nth-child(5) i { background: #6a3b36; }
  .claims li:nth-child(6) i { background: #4a2a28; }

  /* info panels */
  .info-panel { position: absolute; background: var(--panel); }
  .info-panel--ingredients { left: 482px; top: 28px; width: 206px; height: 109px; }
  .info-panel--company { left: 570px; top: 154px; width: 113px; height: 53px; }

  /* seal band */
  .seal-band {
    position: absolute; left: 0; bottom: 0; width: 100%; height: 51px;
    background: linear-gradient(90deg, var(--band-1), var(--band-2) 30%, var(--band-1) 55%, var(--band-2) 80%, var(--band-1));
    display: flex; align-items: center; gap: 20px; padding-left: 10px;
  }
  .seal-band i { width: 28px; height: 18px; border-radius: 50%; flex: none; }
  .seal-band i:nth-child(6n+1) { background: #4a2a28; }
  .seal-band i:nth-child(6n+2) { background: #7a4a44; }
  .seal-band i:nth-child(6n+3) { background: #8c3a36; }
  .seal-band i:nth-child(6n+4) { background: #a83a3a; }
  .seal-band i:nth-child(6n+5) { background: #c23c3c; }
  .seal-band i:nth-child(6n) { background: #d9383c; }
</style>
</head>
<body>
<div class="canvas">

  <section class="surface surface--choc bucket-label bucket-label--choc" role="img" aria-label="Chocolate bucket label on a brushed brown texture">
    <div class="logo"><span class="logo__dot"></span><span class="logo__name">lumé</span></div>
    <ul class="claims">
      <li><i></i>Gluten Free,</li>
      <li><i></i>High Protein,</li>
      <li><i></i>Low Calories,</li>
      <li><i></i>Lactose Free,</li>
      <li><i></i>No Added Sugar,</li>
      <li><i></i>Digestive Enzyme</li>
    </ul>
    <div class="info-panel info-panel--ingredients"></div>
    <div class="info-panel info-panel--company"></div>
    <div class="seal-band"><i></i><i></i><i></i><i></i><i></i><i></i><i></i><i></i><i></i><i></i><i></i><i></i><i></i><i></i><i></i></div>
  </section>

  <section class="surface surface--choc lid lid--choc" role="img" aria-label="Chocolate lid on a brushed brown texture">
    <div class="logo"><span class="logo__dot"></span><span class="logo__name">lumé</span></div>
  </section>

  <div class="logo logo--hero-choc" role="img" aria-label="lumé brand mark, chocolate flavour">
    <span class="logo__dot"></span><span class="logo__name">lumé</span>
  </div>

  <div class="logo logo--hero-vanilla" role="img" aria-label="lumé brand mark, vanilla flavour">
    <span class="logo__dot"></span><span class="logo__name">lumé</span>
  </div>

  <section class="surface surface--vanilla lid lid--vanilla" role="img" aria-label="Vanilla lid on a soft cream texture">
    <div class="logo"><span class="logo__dot"></span><span class="logo__name">lumé</span></div>
  </section>

  <section class="surface surface--vanilla bucket-label bucket-label--vanilla" role="img" aria-label="Vanilla bucket label on a soft cream texture">
    <div class="logo"><span class="logo__dot"></span><span class="logo__name">lumé</span></div>
    <ul class="claims">
      <li><i></i>Gluten Free,</li>
      <li><i></i>High Protein,</li>
      <li><i></i>Low Calories,</li>
      <li><i></i>Lactose Free,</li>
      <li><i></i>No Added Sugar,</li>
      <li><i></i>Digestive Enzyme</li>
    </ul>
    <div class="info-panel info-panel--ingredients"></div>
    <div class="info-panel info-panel--company"></div>
    <div class="seal-band"><i></i><i></i><i></i><i></i><i></i><i></i><i></i><i></i><i></i><i></i><i></i><i></i><i></i><i></i><i></i></div>
  </section>

</div>
</body>
</html>
```